Harmony Swift Care Business card

We want a business card that matches our business theme. Our website is www.swiftcarehub.example
The company name is Harmony Swift Care
The persons having the business cards will be doctors
My logo is attached.
We have a drive-thru medical center where our motto is Fast, Reliable, and Convenient. Our goal is to change the medical space while utilizing technologies, keeping a professional and clean look

Medical

Info on the card should be: Name, Position, Cell number, website, email address, possibly the office line as well

Requirements
Must have
• Logo
Nice to have
• Professional medical feel with our logo colors incorporated

```html
<!DOCTYPE html>
<html lang="en">
<head>
<meta charset="utf-8">
<title>Harmony Swift Care – Business Card</title>
<link rel="stylesheet" href="https://fonts.googleapis.com/css2?family=Mulish:wght@400;600;800&display=swap">
<style>
  :root {
    --bg: #e6e8ec;
    --blue-deep: #1a4aa0;
    --blue-mid: #1f6fc4;
    --blue-light: #2ea3dc;
    --navy: #1c3f94;
    --ink: #3c4250;
    --white: #ffffff;
    --paper: #f7f8fa;
    --ghost: #dfe6f0;
    --rule: #6fb7e6;
  }
  * { box-sizing: border-box; margin: 0; padding: 0; }
  html, body { width: 1200px; height: 900px; overflow: hidden; }
  body {
    background: var(--bg);
    font-family: "Mulish", sans-serif;
    position: relative;
  }
  .card {
    position: absolute;
    left: 260px;
    width: 680px;
    height: 390px;
    border-radius: 34px;
    overflow: hidden;
    box-shadow: 0 10px 28px rgba(0,0,0,0.18);
  }
  /* Front */
  .card--front {
    top: 40px;
    background: radial-gradient(ellipse at 50% 50%, var(--blue-light) 0%, var(--blue-mid) 45%, var(--blue-deep) 100%);
    display: flex;
    flex-direction: column;
    align-items: center;
    justify-content: center;
    color: var(--white);
  }
  .brand {
    display: flex;
    align-items: center;
    gap: 16px;
  }
  .brand__dot {
    width: 58px; height: 58px;
    border-radius: 50%;
    background: currentColor;
    flex: none;
  }
  .brand__name {
    font-weight: 800;
    font-size: 40px;
    line-height: 1;
    letter-spacing: 0.5px;
  }
  .motto {
    margin-top: 16px;
    font-size: 15px;
    font-weight: 600;
    letter-spacing: 1.5px;
  }
  /* Back */
  .card--back {
    top: 470px;
    background: linear-gradient(160deg, var(--white) 0%, var(--paper) 60%, #eceef2 100%);
    color: var(--ink);
  }
  .backdrop-circle {
    position: absolute;
    right: -40px; top: 30px;
    width: 400px; height: 400px;
    border-radius: 50%;
    background: var(--ghost);
    opacity: 0.6;
  }
  .card--back .brand-block {
    position: absolute;
    left: 40px; top: 58px;
    color: var(--navy);
  }
  .card--back .brand__name { font-size: 30px; }
  .card--back .brand__dot { width: 44px; height: 44px; }
  .card--back .motto { color: var(--ink); font-size: 12px; margin-top: 10px; letter-spacing: 1.2px; }
  .person {
    position: absolute;
    right: 380px; bottom: 92px;
    text-align: right;
  }
  .person__role { font-size: 17px; color: var(--ink); }
  .person__name { font-size: 24px; color: var(--navy); font-weight: 600; letter-spacing: 0.5px; margin-top: 2px; }
  .divider {
    position: absolute;
    left: 316px; bottom: 70px;
    width: 1px; height: 110px;
    background: var(--rule);
  }
  .contact {
    position: absolute;
    left: 334px; bottom: 70px;
    list-style: none;
    font-size: 16px;
    color: var(--ink);
  }
  .contact li {
    display: flex; align-items: center; gap: 10px;
    height: 27px;
  }
  .contact svg { width: 16px; height: 16px; flex: none; fill: var(--navy); }
</style>
</head>
<body>
  <section class="card card--front" aria-label="Card front">
    <div class="brand">
      <span class="brand__dot"></span>
      <span class="brand__name">Harmony Swift Care</span>
    </div>
    <p class="motto">FAST | RELIABLE | CONVENIENT</p>
  </section>

  <section class="card card--back" aria-label="Card back">
    <div class="backdrop-circle"></div>
    <div class="brand-block">
      <div class="brand">
        <span class="brand__dot"></span>
        <span class="brand__name">Harmony Swift Care</span>
      </div>
      <p class="motto">FAST | RELIABLE | CONVENIENT</p>
    </div>

    <div class="person">
      <p class="person__role">Director</p>
      <p class="person__name">DANIEL REEVES</p>
    </div>
    <span class="divider"></span>
    <ul class="contact">
      <li><svg viewBox="0 0 16 16"><path d="M5 1h6a1 1 0 0 1 1 1v12a1 1 0 0 1-1 1H5a1 1 0 0 1-1-1V2a1 1 0 0 1 1-1zm0.6 1.6v9.8h4.8V2.6z"/></svg>555 010 234</li>
      <li><svg viewBox="0 0 16 16"><path d="M1 6c0-2 3-3 7-3s7 1 7 3v1h-3.5V5.5h-7V7H1zm3 2h8l2 6H2z"/></svg>(11) 5550 0100</li>
      <li><svg viewBox="0 0 16 16"><path d="M1 4h14v9H1zm1.5 1.2L8 9l5.5-3.8V5H2.5z"/></svg>daniel@swiftcarehub.example</li>
      <li><svg viewBox="0 0 16 16"><path d="M8 1a7 7 0 1 0 0 14A7 7 0 0 0 8 1zm0 1.5a5.5 5.5 0 0 1 4.8 2.8H10L8.5 7 6 6.5 4.5 8l1.5 2 2 .5-.5 3A5.5 5.5 0 0 1 8 2.5z"/></svg>www.swiftcarehub.example</li>
    </ul>
  </section>
</body>
</html>
```